STANDDESIGN FÜR PODIUMCASE, ROLL-UP & TISCHAUFSTELLER
"STANDDESIGN" FÜR PODIUMCASE, ROLL-UP & TISCHAUFSTELLER
Zielgruppe
Primär Raucher, die gerne überall rauchen würden, wenn sie dürften und gleichzeitig innovativ genug für eine "neue" Art des Rauchens sind.
Personen über 18 Jahre!!!
Aufgabenstellung
Für unsere elektronische Zigarette Lunaro wollen wir eine Art Mini-Werbe-Stand. Dieser wird aus folgenden Dingen bestehen:
- 1 Podium Case
- 2 Roll-Ups
Dazu als passend ein Tischaufsteller.
Der "Mini-Werbestand" soll emotional die Themen Rauchen, Rauchverbot, Rauchgenuss transportieren und diese dann positiv auf unsere elektronische Zigarette lenken, die überall konsumiert werden darf.
Weitere Informationen über unser Produkt: http://www.lunaro.biz

```html
<!DOCTYPE html>
<html lang="de">
<head>
<meta charset="utf-8">
<title>Lunaro – Roll-Ups</title>
<link rel="stylesheet" href="https://fonts.googleapis.com/css2?family=Exo+2:ital,wght@1,400&family=Marcellus&family=Open+Sans:ital,wght@0,400;1,400&display=swap">
<style>
  :root {
    --navy: #12173a;
    --navy-edge: #1b2150;
    --paper: #ffffff;
    --paper-soft: #f1f2f3;
    --ink: #1a1c2c;
    --accent: #f06a1a;
    --frame: #1b1d3a;
    --filter: #c99a2e;
    --filter-dark: #a57416;
    --stick: #f3f3f3;
    --stick-shade: #c9c9c9;
  }
  * { margin: 0; padding: 0; box-sizing: border-box; }
  html, body { width: 1200px; height: 900px; overflow: hidden; background: var(--paper); }
  .canvas { position: relative; width: 1200px; height: 900px; background: var(--paper); }
  .outer-frame {
    position: absolute; left: 14px; top: 12px; width: 1172px; height: 876px;
    border: 2px solid var(--frame);
  }
  .rollup {
    position: absolute; top: 33px; width: 352px; height: 832px;
    background: var(--navy);
  }
  .rollup--info { left: 257px; }
  .rollup--claim { left: 623px; }
  .rollup__surface {
    position: absolute; inset: 10px;
    background: var(--paper);
    box-shadow: 0 0 8px 6px rgba(255,255,255,0.85);
    border-radius: 3px;
  }
  .rollup--claim .rollup__surface { background: var(--paper-soft); }
  .brand-block {
    position: absolute; left: 19px; width: 314px;
    background: var(--navy);
    box-shadow: 0 0 6px 2px var(--navy-edge);
  }
  .rollup--info .brand-block { top: 20px; height: 261px; }
  .rollup--claim .brand-block { top: 553px; height: 258px; }
  .brand-name {
    position: absolute; left: 0; right: 0;
    text-align: center;
    font-family: "Marcellus", serif;
    font-size: 48px; color: var(--paper);
    letter-spacing: 1px;
  }
  .rollup--info .brand-name { top: 162px; }
  .rollup--claim .brand-name { top: 172px; }
  .body-copy {
    position: absolute; left: 66px; top: 297px; width: 272px;
    font-family: "Open Sans", sans-serif; font-style: italic;
    font-size: 9.6px; line-height: 13.2px; color: var(--ink);
  }
  .tagline {
    position: absolute;
    font-family: "Open Sans", sans-serif;
    font-size: 15px; line-height: 19px; color: var(--ink);
    letter-spacing: 0.3px;
  }
  .rollup--info .tagline { left: 149px; top: 592px; }
  .rollup--claim .tagline { left: 103px; top: 423px; font-size: 16px; line-height: 21px; }
  .web {
    position: absolute; left: 0; right: 0; text-align: center;
    font-family: "Open Sans", sans-serif; font-style: italic;
    font-size: 15px; letter-spacing: 1px; color: var(--ink);
  }
  .rollup--info .web { top: 782px; }
  .rollup--claim .web { top: 518px; }
  .product {
    position: absolute; width: 300px; height: 42px;
    transform-origin: left center; transform: rotate(11deg);
    display: flex; border-radius: 4px 10px 10px 4px; overflow: hidden;
    box-shadow: 0 8px 10px rgba(0,0,0,0.18);
  }
  .rollup--info .product { left: 30px; top: 645px; }
  .rollup--claim .product { left: 46px; top: 312px; }
  .product__tip { width: 30%; background: linear-gradient(180deg, var(--filter) 0%, var(--filter-dark) 100%); }
  .product__body { flex: 1; background: linear-gradient(180deg, var(--stick) 0%, var(--paper) 40%, var(--stick-shade) 100%); }
  .headline {
    position: absolute; left: 42px; top: 50px;
    font-family: "Exo 2", sans-serif; font-style: italic;
    font-size: 19px; line-height: 31px; letter-spacing: 2px; color: var(--ink);
  }
  .benefits { position: absolute; left: 44px; top: 165px; list-style: none; }
  .benefit {
    display: flex; gap: 18px; margin-bottom: 10px;
    font-family: "Exo 2", sans-serif; font-style: italic;
    font-size: 13px; line-height: 21px; letter-spacing: 1.2px; color: var(--ink);
  }
  .benefit__mark { width: 18px; flex: none; margin-top: 5px; }
</style>
</head>
<body>
<div class="canvas">
  <div class="outer-frame"></div>

  <section class="rollup rollup--info">
    <div class="rollup__surface"></div>
    <div class="brand-block"><div class="brand-name">Lunaro</div></div>
    <p class="body-copy">Elektronische Zigaretten erzeugen keinen Passivrauch! Der sichtbar ausgeatmete Dampf besteht fast nur aus geruchsneutralem Wasserdampf und minimalen Spuren von Nikotin und Propandiol in nicht schädlichen Dosen. Dies hat Vita Research Aotearoa (gegründet vom ehemaligen Leiter des Gesundheitsministeriums von Neuseeland, Dr.Harold Penwick) in ihrer Studie vom 08. September 2010 bestätigt (http://www.vitaresearch.example/ ECigsExhaledSmoke.htm) und kam zu dem Ergebnis: Second hand mist from an ecigarette is not smoke at all, and does not contain any substance known to cause death, short or long term, in the quantities found. (Passivrauch von elektronischen Zigaretten ist kein Rauch und enthält keinerlei bekannte Substanzen oder kritische Mengen von Substanzen, die zu kurz- oder langzeitigen Schädigungen führen.)</p>
    <p class="tagline">Mit<br>geniesen Sie wieder<br>ein Stuck Freiheit</p>
    <div class="product" role="img" aria-label="Produktfoto der elektronischen Zigarette">
      <div class="product__tip"></div><div class="product__body"></div>
    </div>
    <div class="web">www.lunaro.biz</div>
  </section>

  <section class="rollup rollup--claim">
    <div class="rollup__surface"></div>
    <h1 class="headline">Die Genussalternative<br>zur herkommlichen<br>Zigarette</h1>
    <ul class="benefits">
      <li class="benefit">
        <svg class="benefit__mark" viewBox="0 0 18 18" aria-hidden="true"><path d="M3 3 L15 15 M15 3 L3 15" stroke="var(--accent)" stroke-width="3" stroke-linecap="round"/></svg>
        <span>onhe hohe mengen an<br>schadlichen Zusatzstoffen</span>
      </li>
      <li class="benefit">
        <svg class="benefit__mark" viewBox="0 0 18 18" aria-hidden="true"><path d="M3 3 L15 15 M15 3 L3 15" stroke="var(--accent)" stroke-width="3" stroke-linecap="round"/></svg>
        <span>enthalt keinerlei bekannte<br>Substanzen die zu<br>fuhrenSchadigungen</span>
      </li>
    </ul>
    <div class="product" role="img" aria-label="Produktfoto der elektronischen Zigarette">
      <div class="product__tip"></div><div class="product__body"></div>
    </div>
    <p class="tagline">Mit us durfen<br>Sie wieder uberall<br>rauchen</p>
    <div class="web">www.lunaro.biz</div>
    <div class="brand-block"><div class="brand-name">Lunaro</div></div>
  </section>
</div>
</body>
</html>
```